Poster displaybox & poster box sticker

We need a graphic design for a displaybox for posters in suvenir shop.

On picture #1 (on left) you can see existing displaybox, which has a design we are not happy with. On pictures #2, #3, #4, #5 you can see poster designs that we are trying to sell (some or all of those posters should be on that displaybox. We feel that poster design on picture #2 is most attractive for our customers, and it should be displayed in front side of the box but we are open for suggestions). We can provide pictures with better and higher resolution if needed.

On Picture #1 (on right) you can see box which contains poster. We need graphic design for a sticker for that box. The sticker should represent the poster design which is in the box (pictures #2,#3,#4,#5). The sticker design should be compatible with the displaybox design.

Industry/Entity Type

Graphic Design

Requirements
Must have
• measures for displaybox are 28cmX16cmX28cm (lengh, width, depth), see picture #1

displaybox should display text "KESTRAVEL ART POSTER" because it is the name of our product (posters that we are trying to sell)

measures of the box for posters are 4,5cmx4,5cmx49cm and it is already made. We need a sticker that should go on that box which represents the poster design containing. Essentialy it is going to be 4 differerent stickers (for each post poster design containing) but with the same design. We feel it should be a sticker that goes around the box but we are open for any suggestions.
Nice to have
• we feel some of the design of box and sticker shoud have red color, but we are open for suggestions

```html
<!DOCTYPE html>
<html lang="en">
<head>
<meta charset="utf-8">
<title>Kestravel Art Poster – Box Stickers</title>
<link rel="stylesheet" href="https://fonts.googleapis.com/css2?family=Cinzel:wght@400&family=Playfair+Display:wght@400&display=swap">
<style>
  :root {
    --paper: #ffffff;
    --badge: #a3481d;
    --badge-ink: #fdf3c8;
    --purple: #a22fe0;
    --brown: #8e4a1c;
    --lime: #c8f21a;
    --yellow: #fbf55a;
    --orange: #ff8a2e;
    --teal: #49f5c0;
  }
  * { box-sizing: border-box; margin: 0; padding: 0; }
  html, body {
    width: 829px;
    height: 1200px;
    overflow: hidden;
    background: var(--paper);
  }
  .sheet {
    position: relative;
    width: 829px;
    height: 1200px;
  }
  .sticker {
    position: absolute;
    left: 0;
    width: 800px;
    height: 236px;
  }
  .sticker--1 { top: 11px; }
  .sticker--2 { top: 295px; }
  .sticker--3 { top: 579px; }
  .sticker--4 { top: 865px; }

  .sticker__band {
    position: absolute;
    left: 0;
    top: 44px;
    width: 800px;
    height: 148px;
    background: linear-gradient(
      to bottom,
      var(--purple) 0%,
      var(--brown) 14%,
      var(--lime) 28%,
      var(--yellow) 40%,
      var(--orange) 50%,
      var(--yellow) 60%,
      var(--teal) 72%,
      var(--brown) 86%,
      var(--purple) 100%
    );
    opacity: 0.85;
  }

  .badge {
    position: absolute;
    left: 319px;
    top: 0;
    width: 162px;
    height: 236px;
    border-radius: 50%;
    background: var(--badge);
    color: var(--badge-ink);
    text-align: center;
  }
  .badge__number {
    display: block;
    margin-top: 36px;
    font-family: "Playfair Display", serif;
    font-size: 88px;
    font-weight: 400;
    line-height: 1;
  }
  .badge__name {
    display: block;
    margin: 24px auto 0;
    width: 120px;
    font-family: "Cinzel", serif;
    font-size: 13px;
    font-weight: 400;
    letter-spacing: 0.5px;
    line-height: 1.3;
  }
</style>
</head>
<body>
<main class="sheet">

  <section class="sticker sticker--1">
    <div class="sticker__band" role="img" aria-label="Band of colourful diamond pattern in purple, brown, lime, yellow, orange and teal"></div>
    <div class="badge">
      <span class="badge__number">1</span>
      <span class="badge__name">Kestravel Art Posters</span>
    </div>
  </section>

  <section class="sticker sticker--2">
    <div class="sticker__band" role="img" aria-label="Band of colourful diamond pattern in purple, brown, lime, yellow, orange and teal"></div>
    <div class="badge">
      <span class="badge__number">2</span>
      <span class="badge__name">Kestravel Art Posters</span>
    </div>
  </section>

  <section class="sticker sticker--3">
    <div class="sticker__band" role="img" aria-label="Band of colourful diamond pattern in purple, brown, lime, yellow, orange and teal"></div>
    <div class="badge">
      <span class="badge__number">3</span>
      <span class="badge__name">Kestravel Art Posters</span>
    </div>
  </section>

  <section class="sticker sticker--4">
    <div class="sticker__band" role="img" aria-label="Band of colourful diamond pattern in purple, brown, lime, yellow, orange and teal"></div>
    <div class="badge">
      <span class="badge__number">4</span>
      <span class="badge__name">Kestravel Art Posters</span>
    </div>
  </section>

</main>
</body>
</html>
```